Flyer für Immobilienmakler
Zielgruppe
Wir, die Wendtal Immobilien GmbH, vermitteln Häuser, Wohnungen und Grundstücke, unsere Zielgruppe sind Verkäufer und Kaufinteressenten aus der Region, Immobilien zur Vermittlung gesucht
Aufgabenstellung
Unverbindliche Ersteinschätzung, Ansprechpartner vor Ort, regionale Marktkenntnis. Max. Din A 5, Immobilien zur Vermittlung gesucht.
- Flyer nur zur Immobilienvermittlung

```html
<!DOCTYPE html>
<html lang="de">
<head>
<meta charset="utf-8">
<title>Wendtal Immobilien GmbH – Flyer</title>
<link href="https://fonts.googleapis.com/css2?family=Montserrat:wght@400;700&display=swap" rel="stylesheet">
<style>
  :root{
    --grey:#8b8b8b;
    --green:#2aa57a;
    --purple:#6a5fa3;
    --cream:#fdf9f3;
    --ink:#3a3a3a;
    --white:#ffffff;
    --photo-top:#9dbbe0;
    --photo-bottom:#8fb98a;
  }
  *{margin:0;padding:0;box-sizing:border-box}
  html,body{width:849px;height:1200px;overflow:hidden;background:var(--grey)}
  body{font-family:'Montserrat',sans-serif;color:var(--white)}
  .flyer{position:relative;width:849px;height:1200px;background:var(--grey);overflow:hidden}
  .hero-photo{position:absolute;left:0;top:0;width:849px;height:600px;
    background:linear-gradient(180deg,var(--photo-top) 0%,var(--photo-bottom) 100%)}
  .brand-box{position:absolute;left:396px;top:0;width:385px;height:164px;background:var(--cream);
    display:flex;align-items:center;justify-content:center}
  .brand-name{font-weight:700;font-size:21px;color:var(--ink);letter-spacing:.3px}
  .content{position:absolute;left:65px;top:620px;width:525px}
  .headline{font-weight:400;font-size:41px;line-height:50px;letter-spacing:4.6px;text-transform:uppercase}
  .tagline{font-size:21px;letter-spacing:5.6px;margin-top:4px}
  .intro-title{font-weight:700;font-size:16.5px;margin-top:28px;letter-spacing:.2px}
  .intro-text{font-size:15px;line-height:21.5px;letter-spacing:1.1px;text-align:justify}
  .benefits{list-style:none;margin:12px 0 0 24px}
  .benefits li{font-size:15px;line-height:21.4px;letter-spacing:1.4px;position:relative;padding-left:20px}
  .benefits li::before{content:"";position:absolute;left:2px;top:9px;width:5px;height:5px;border-radius:50%;background:var(--white)}
  .cta-title{font-weight:700;font-size:16.5px;margin-top:14px;letter-spacing:.3px}
  .cta-text{font-size:15px;line-height:21.5px;letter-spacing:1.1px}
  .feature-card{position:absolute;left:615px;width:166px;background:var(--cream);color:var(--ink);
    text-align:center;font-size:16px;line-height:21.5px;letter-spacing:.6px}
  .feature-card strong{font-weight:700}
  .feature-card svg{display:block;margin:0 auto}
  .card-search{top:569px;height:167px;padding-top:18px}
  .card-region{top:741px;height:166px;padding-top:15px}
  .card-care{top:913px;height:165px;padding-top:15px}
  .card-search .label{margin-top:12px}
  .card-region .label{margin-top:17px}
  .card-care .label{margin-top:10px}
  .footer-rule{position:absolute;left:0;top:1103px;width:849px;height:5px;background:var(--green)}
  .footer{position:absolute;left:0;top:1108px;width:849px;height:92px;background:var(--purple);
    text-align:center;font-size:23px;line-height:36px;padding-top:12px;letter-spacing:.4px}
</style>
</head>
<body>
<div class="flyer">
  <div class="hero-photo" role="img" aria-label="Foto: Landhaus mit Ziegeldach, Garten und Pool unter blauem Sommerhimmel"></div>

  <div class="brand-box"><span class="brand-name">Wendtal Immobilien GmbH</span></div>

  <section class="content">
    <h1 class="headline">Ihre Immobilie<br>in guten Händen</h1>
    <p class="tagline">Regional. Persönlich. Kompetent</p>
    <h2 class="intro-title">Sie denken über den Verkauf Ihrer Immobilie nach?</h2>
    <p class="intro-text">Die Wendtal Immobilien GmbH begleitet Sie persönlich und kompetent – von der unverbindlichen Ersteinschätzung bis zur erfolgreichen Vermittlung.</p>
    <ul class="benefits">
      <li>Unverbindliche Ersteinschätzung Ihrer Immobilie</li>
      <li>Persönlicher Ansprechpartner in Ihrer Region</li>
      <li>Fundierte regionale Marktkenntnis</li>
      <li>Transparente Beratung &amp; realistische Preisfindung</li>
      <li>Seriöse Vermittlung ohne Verkaufsdruck</li>
    </ul>
    <h2 class="cta-title">Jetzt unverbindlich beraten lassen</h2>
    <p class="cta-text">Vereinbaren Sie gerne einen persönlichen Termin –<br>wir nehmen uns Zeit für Ihr Anliegen.</p>
  </section>

  <div class="feature-card card-search">
    <svg width="70" height="62" viewBox="0 0 70 62" aria-hidden="true">
      <path d="M35 3 L68 32 L60 32 L60 58 L10 58 L10 32 L2 32 Z" fill="var(--green)"/>
      <rect x="14" y="6" width="6" height="14" fill="var(--green)"/>
      <rect x="30" y="38" width="12" height="20" rx="2" fill="#e9efe9"/>
    </svg>
    <p class="label"><strong>Immobilien zur Vermittlung</strong><br>gesucht</p>
  </div>

  <div class="feature-card card-region">
    <svg width="50" height="50" viewBox="0 0 50 50" aria-hidden="true">
      <circle cx="25" cy="25" r="24" fill="var(--green)"/>
      <path d="M25 37 C19 29 17 25 17 21 A8 8 0 0 1 33 21 C33 25 31 29 25 37 Z" fill="none" stroke="#ffffff" stroke-width="1.6"/>
      <circle cx="25" cy="21" r="3" fill="none" stroke="#ffffff" stroke-width="1.6"/>
    </svg>
    <p class="label">Zentral im<br><strong>Raum Lindbach und Umgebung</strong></p>
  </div>

  <div class="feature-card card-care">
    <svg width="56" height="50" viewBox="0 0 56 50" aria-hidden="true">
      <ellipse cx="20" cy="30" rx="16" ry="11" fill="none" stroke="var(--green)" stroke-width="3"/>
      <path d="M10 39 L6 48 L18 41" fill="none" stroke="var(--green)" stroke-width="3"/>
      <ellipse cx="34" cy="20" rx="19" ry="14" fill="#ffffff" stroke="var(--green)" stroke-width="3"/>
      <path d="M42 32 L47 42 L34 34" fill="#ffffff" stroke="var(--green)" stroke-width="3"/>
    </svg>
    <p class="label"><strong>Individuelle Betreuung</strong><br>statt Massen-<br>abfertigung</p>
  </div>

  <div class="footer-rule"></div>
  <footer class="footer">
    <p>Wendtal Immobilien GmbH · Mühlenweg 7 · 84999 Lindbach</p>
    <p>www.wendtal-immobilien.de · Tel. +49 85 00 123450-0</p>
  </footer>
</div>
</body>
</html>
```